Flyer Design Project - Financial services business specialising in mortgages and insurance

I require a flyer to create interest in saving money with mortgages. We show people that they can save money on their mortgages by paying the mortgage of sooner. Therefore they no longer need to work for the bank, and that they can live their life debt free.
The call to action is that they pick up the phone and call me or make an inquiry online via our website.

We are a insurance and mortgage brokerage and the business name is called BRAVO. Website: www.bravolenders.co.nz (currently)
the new website that isn't quite live yet is viewable at
www.qortasites.com/bravo

Our tag line is Hearth Growth Tomorrow

The type of clients we are trying to engage with are home owners with existing mortgages.

Aged between 35-40, Professionals, Income bracket of $80k plus for the household, in a relationship, no more than two kids, live in our local area (West Auckland, New Zealand) they are driven to be successful and have a comfortable family life and be able to afford luxuries.(responsible)

We would like to see what options someone can come up other than the ususal. Needs to fit with our business name BRAVO + Tag line. As in we do things BRAVOER.

The flyer needs to show that we can help make a difference.

We will provide a free comparative market report on their house for an appointment and also if we cant save the prospect any money our guarantee is that we will give them a $20 voucher. (conditions will apply).

Ideally looking to have the flyer on a DLE size although we are open to options.

more than happy to discuss further if required to. I have attached my logo and my current image for home loans used on the website although i would like to see if there are any better options available than my current image.

Reason: Waiting on a couple of other designers who were sending there designs through before closing of.

Target Market(s)

home owners with an existing mortgage. Ages between 35-40, Professionals, Income 80k+

Industry/Entity Type

Insurance

Requirements
Must have
• A disclosure document is available upon request.
Our logo and contact details.
Call to action
Nice to have
• Want to focus on the lifestyles and goals rather than the actual payment of the mortgage.
Should not have
• We don't want to be saying the same boring message as most mortgage brokers are saying ie. Call us we can save you thousands of dollars.
We a need a reason for them to call us to go with our image and brand.

```html
<!DOCTYPE html>
<html lang="en">
<head>
<meta charset="utf-8">
<title>BRAVO – Want a Bravoer Future?</title>
<link rel="stylesheet" href="https://fonts.googleapis.com/css2?family=Varela+Round&family=Source+Sans+3:wght@400;600;700&family=Baloo+2:wght@800&display=swap">
<style>
  :root {
    --sky-blue: #2f8ff0;
    --headline-blue: #2e8cf0;
    --violet: #a43ff2;
    --box-blue: #3a90f2;
    --salmon: #f48a6c;
    --white: #ffffff;
    --bg-light: #ffffff;
    --bg-edge: #e4e4e4;
    --tagline: #3f6c9a;
    --tile-teal: #6fd8d8;
    --tile-blue: #2e63c8;
  }
  * { margin: 0; padding: 0; box-sizing: border-box; }
  html, body { width: 1200px; height: 2544px; overflow: hidden; }
  body {
    position: relative;
    background: radial-gradient(ellipse at 50% 40%, var(--bg-light) 0%, #f4f4f4 55%, var(--bg-edge) 100%);
    font-family: "Source Sans 3", Arial, sans-serif;
  }
  .headline {
    position: absolute; left: 0; top: 20px; width: 1200px;
    text-align: center; color: var(--headline-blue);
    font-family: "Varela Round", Arial, sans-serif;
  }
  .headline-lead { font-size: 64px; line-height: 1; letter-spacing: 1px; }
  .headline-main { font-size: 228px; line-height: 0.8; margin-top: 14px; letter-spacing: -2px; }
  .hero-image {
    position: absolute; left: 24px; top: 525px; width: 660px; height: 540px;
    border-radius: 40% 40% 30% 30%;
    background: linear-gradient(180deg, #e23a4a 0%, #e23a4a 36%, #f2a0e6 37%, #e58ad8 80%, #f4f4f4 100%);
  }
  .call-badge {
    position: absolute; left: 796px; top: 530px; width: 380px; height: 380px;
    border-radius: 50%; background: var(--salmon);
    display: flex; flex-direction: column; align-items: center; justify-content: center;
    color: var(--white); font-family: "Baloo 2", Arial, sans-serif; font-weight: 800;
    transform: rotate(12deg); line-height: 0.95;
  }
  .call-badge .small { font-size: 86px; }
  .call-badge .big { font-size: 96px; }
  .promise-box {
    position: absolute; left: 47px; top: 1155px; width: 1108px; height: 382px;
    background: var(--violet); color: var(--white);
    display: flex; align-items: center; justify-content: center; text-align: center;
    font-size: 82px; font-weight: 600; line-height: 1.2;
  }
  .freedom-box {
    position: absolute; left: 47px; top: 1569px; width: 1108px; height: 222px;
    background: var(--box-blue); color: var(--white);
    display: flex; align-items: center; justify-content: center; text-align: center;
    font-size: 66px; font-weight: 600; line-height: 1.18;
  }
  .offer-note {
    position: absolute; left: 40px; top: 1822px; width: 1120px;
    text-align: center; color: var(--sky-blue);
    font-size: 33px; font-weight: 600; line-height: 1.3;
  }
  .offer-note .conditions { font-size: 25px; }
  .web-address {
    position: absolute; left: 0; top: 2000px; width: 1200px; text-align: center;
    color: var(--salmon); font-size: 70px; font-weight: 700; letter-spacing: 1px;
  }
  .phone-number {
    position: absolute; left: 340px; top: 2095px; width: 780px; text-align: center;
    color: var(--salmon); font-size: 112px; font-weight: 700; letter-spacing: 4px;
  }
  .brand-mark { position: absolute; left: 80px; top: 2250px; color: var(--headline-blue); }
  .brand-name {
    font-family: "Varela Round", Arial, sans-serif; font-size: 150px; line-height: 1;
  }
  .brand-tagline {
    font-family: "Varela Round", Arial, sans-serif; color: var(--tagline);
    font-size: 40px; margin-top: 14px; margin-left: 10px;
  }
  .social-tile {
    position: absolute; top: 2285px; width: 190px; height: 180px;
    border-radius: 22px;
  }
  .social-tile.teal { left: 700px; background: var(--tile-teal); }
  .social-tile.blue { left: 922px; background: var(--tile-blue); }
</style>
</head>
<body>
  <header class="headline">
    <div class="headline-lead">Want a</div>
    <div class="headline-main">Bravoer<br>Future?</div>
  </header>

  <div class="hero-image" role="img" aria-label="Pink piggy bank wearing a red house roof with a chimney"></div>

  <div class="call-badge">
    <span class="small">Call us</span>
    <span class="big">TODAY</span>
  </div>

  <section class="promise-box">
    <p>Save money on your<br>mortgage and enjoy a<br>brighter future.</p>
  </section>

  <section class="freedom-box">
    <p>Pay off your mortgage sooner<br>and stop working for the bank.</p>
  </section>

  <p class="offer-note">We will provide a free comparative market report on your<br>house and if we cant save you any money our guarantee<br>is that we will give them a $20 voucher. <span class="conditions">(conditions will apply).</span></p>

  <div class="web-address">www.qortasites.com/bravo</div>
  <div class="phone-number">09 555 0142</div>

  <div class="brand-mark">
    <div class="brand-name">BRAVO</div>
    <div class="brand-tagline">Hearth Growth Tomorrow</div>
  </div>

  <div class="social-tile teal" role="img" aria-label="Social media link"></div>
  <div class="social-tile blue" role="img" aria-label="Social media link"></div>
</body>
</html>
```